Stonegate Towing Business Card

Towing
Accident towing
Mechanical breakdown
Insurance, salvage and recovery
4wd off road towing
Light & Heavy towing
7354 2618
24 hour business 7 days

Logo can be whole size on front

Industry/Entity Type

Towing/ transport

Contact Information for Business Card

The above

```html
<!DOCTYPE html>
<html lang="en">
<head>
<meta charset="utf-8">
<title>Stonegate Towing Business Card</title>
<link href="https://fonts.googleapis.com/css2?family=Oswald:wght@400;700&display=swap" rel="stylesheet">
<style>
  :root {
    --backdrop: #adadad;
    --brand-red: #d3202a;
    --card-white: #ffffff;
    --ink: #111111;
    --navy: #1f3a5f;
    --shadow: rgba(0, 0, 0, 0.35);
  }
  html, body {
    margin: 0;
    padding: 0;
    overflow: hidden;
  }
  body {
    width: 1200px;
    height: 1000px;
    background: var(--backdrop);
    position: relative;
    font-family: "Oswald", sans-serif;
  }
  .card {
    position: absolute;
    width: 694px;
    height: 398px;
    border-radius: 26px;
    box-shadow: 8px 8px 14px var(--shadow);
    overflow: hidden;
  }
  .card--front {
    left: 248px;
    top: 86px;
    background: var(--brand-red);
    display: flex;
    align-items: center;
    justify-content: center;
  }
  .front-name {
    color: var(--card-white);
    font-weight: 700;
    font-size: 74px;
    letter-spacing: 1px;
    text-transform: uppercase;
    margin: 0;
  }
  .card--back {
    left: 251px;
    top: 530px;
    background: var(--card-white);
  }
  .back-name {
    position: absolute;
    left: 62px;
    top: 118px;
    width: 228px;
    margin: 0;
    color: var(--brand-red);
    font-weight: 700;
    font-size: 40px;
    line-height: 1.05;
    text-transform: uppercase;
    text-align: center;
  }
  .services {
    position: absolute;
    left: 328px;
    top: 72px;
    margin: 0;
    padding: 0;
    list-style: none;
    color: var(--ink);
    font-size: 26px;
    font-weight: 400;
    line-height: 35px;
  }
  .services li {
    position: relative;
    padding-left: 22px;
  }
  .services li::before {
    content: "";
    position: absolute;
    left: 0;
    top: 15px;
    width: 9px;
    height: 9px;
    border-radius: 50%;
    background: var(--brand-red);
  }
  .hours-badge {
    position: absolute;
    left: 560px;
    top: 58px;
  }
  .divider {
    position: absolute;
    left: 14px;
    right: 15px;
    top: 327px;
    border-top: 1px solid var(--ink);
  }
  .contact {
    position: absolute;
    left: 0;
    right: 0;
    top: 340px;
    display: flex;
    align-items: center;
    justify-content: center;
    gap: 12px;
  }
  .contact-phone {
    color: var(--brand-red);
    font-weight: 700;
    font-size: 38px;
    line-height: 44px;
    letter-spacing: 0.5px;
  }
</style>
</head>
<body>
  <section class="card card--front">
    <h1 class="front-name">Stonegate Towing</h1>
  </section>

  <section class="card card--back">
    <h2 class="back-name">Stonegate<br>Towing</h2>

    <ul class="services">
      <li>Towing</li>
      <li>Accident towing</li>
      <li>Mechanical breakdown</li>
      <li>Insurance, salvage and recovery</li>
      <li>4wd off road towing</li>
      <li>Light &amp; Heavy towing</li>
    </ul>

    <svg class="hours-badge" width="112" height="70" viewBox="0 0 112 70" aria-label="Open 24/7">
      <path d="M58 16 A28 28 0 1 0 40 63" fill="none" stroke="var(--brand-red)" stroke-width="5" stroke-linecap="round"/>
      <line x1="30" y1="37" x2="30" y2="20" stroke="var(--brand-red)" stroke-width="3" stroke-linecap="round"/>
      <line x1="30" y1="37" x2="18" y2="37" stroke="var(--brand-red)" stroke-width="3" stroke-linecap="round"/>
      <text x="68" y="25" font-family="Oswald, sans-serif" font-weight="700" font-size="12" fill="var(--navy)">OPEN</text>
      <text x="42" y="58" font-family="Oswald, sans-serif" font-weight="700" font-size="28" fill="var(--brand-red)">24/7</text>
    </svg>

    <div class="divider"></div>

    <div class="contact">
      <svg width="34" height="34" viewBox="0 0 34 34" aria-hidden="true">
        <circle cx="17" cy="17" r="17" fill="var(--ink)"/>
        <path d="M11 9.5c1-.8 2-.6 2.6.3l1.6 2.4c.5.8.3 1.6-.4 2.2l-1 .8c.8 1.8 2.2 3.3 4 4.2l.9-1c.6-.7 1.5-.8 2.2-.3l2.4 1.6c.9.6 1 1.7.2 2.6l-1 1.1c-1 1-2.6 1.3-4 .6-4-1.9-6.9-4.9-8.6-8.8-.6-1.4-.3-3 .8-4z" fill="var(--card-white)"/>
      </svg>
      <span class="contact-phone">7354-2618</span>
    </div>
  </section>
</body>
</html>
```